BRIM Outreach Partners Business Card Rebrand

Hello Designers! We are looking for help designing our new business card to go in conjunction with our company rebrand. Unfortunately, we have an event mid June that requires we get these printed ASAP (before our new website is launched.) We have a mostly complete Brand Book which I have uploaded to this request for your reference to company information, style, fonts. I've also enclosed our logo file in .eps & .jpg. Attached is a sample business card my boss liked but said was "too simple." I made it in Canva and do not profess to be a designer. NOT FOR DESIGN REFERENCE, ONLY FOR CONTEXT Here is what our old website looks like: https://brimoutreachpartners.com/.

```html
<!DOCTYPE html>
<html lang="en">
<head>
<meta charset="utf-8">
<title>BRIM Outreach Partners – Business Card</title>
<link href="https://fonts.googleapis.com/css2?family=Montserrat:wght@300;400;700&display=swap" rel="stylesheet">
<style>
  :root {
    --backdrop: #5a5656;
    --card: #1b1b1c;
    --card-edge: #111112;
    --accent: #45b3e6;
    --ink-light: #f2f2f2;
    --ink-muted: #d8d8d8;
    --gloss: #0f0f10;
  }
  * { box-sizing: border-box; margin: 0; padding: 0; }
  html, body { width: 1200px; height: 912px; overflow: hidden; }
  body {
    background: var(--backdrop);
    font-family: "Montserrat", sans-serif;
    display: flex;
    flex-direction: column;
    align-items: center;
    justify-content: center;
    gap: 40px;
  }
  .card {
    position: relative;
    width: 700px;
    height: 400px;
    background: radial-gradient(ellipse at 40% 35%, #232324 0%, var(--card) 60%, var(--card-edge) 100%);
    box-shadow: 0 10px 28px rgba(0,0,0,.45);
  }

  /* front */
  .card-front .brand {
    position: absolute;
    left: 50%; top: 50%;
    transform: translate(-50%, -50%);
    display: flex;
    align-items: center;
    gap: 18px;
  }
  .brand-dot {
    width: 96px; height: 96px;
    border-radius: 50%;
    background: var(--accent);
    flex: none;
  }
  .card-front .brand-name {
    font-weight: 700;
    font-size: 34px;
    line-height: 1.05;
    color: var(--gloss);
    width: 250px;
  }

  /* back */
  .card-back .brand {
    position: absolute;
    left: 40px; top: 58px;
    display: flex;
    align-items: center;
    gap: 14px;
  }
  .card-back .brand-dot { width: 74px; height: 74px; }
  .card-back .brand-name {
    font-weight: 700;
    font-size: 25px;
    line-height: 1.05;
    color: var(--ink-light);
    width: 200px;
  }
  .person {
    position: absolute;
    right: 42px; top: 92px;
    text-align: right;
  }
  .person-name {
    font-weight: 700;
    font-size: 25px;
    color: var(--accent);
    letter-spacing: .2px;
  }
  .person-role {
    font-weight: 400;
    font-size: 15px;
    color: var(--ink-muted);
    margin-top: 2px;
  }
  .rule {
    position: absolute;
    left: 230px; right: 36px; top: 188px;
    height: 2px;
    background: var(--accent);
  }
  .location {
    position: absolute;
    right: 42px; top: 214px;
    text-align: right;
    font-weight: 300;
    font-size: 16px;
    line-height: 1.35;
    color: var(--ink-light);
  }
  .contacts {
    position: absolute;
    left: 230px; bottom: 36px;
    list-style: none;
  }
  .contacts li {
    display: flex;
    align-items: center;
    gap: 10px;
    font-weight: 300;
    font-size: 19px;
    color: var(--ink-light);
    line-height: 1.5;
  }
  .contacts svg { width: 14px; height: 14px; flex: none; }
</style>
</head>
<body>

  <section class="card card-front" aria-label="Card front">
    <div class="brand">
      <span class="brand-dot"></span>
      <span class="brand-name">BRIM Outreach Partners</span>
    </div>
  </section>

  <section class="card card-back" aria-label="Card back">
    <div class="brand">
      <span class="brand-dot"></span>
      <span class="brand-name">BRIM Outreach Partners</span>
    </div>

    <div class="person">
      <div class="person-name">Daniel Morrow-Pike</div>
      <div class="person-role">Managing Partner</div>
    </div>

    <div class="rule"></div>

    <div class="location">Denver, CO based<br>( Mountain Time )</div>

    <ul class="contacts">
      <li>
        <svg viewBox="0 0 24 24" aria-hidden="true"><path fill="#45b3e6" d="M6.6 10.8a15.2 15.2 0 0 0 6.6 6.6l2.2-2.2a1 1 0 0 1 1-.25 11.4 11.4 0 0 0 3.6.57 1 1 0 0 1 1 1V20a1 1 0 0 1-1 1A17 17 0 0 1 3 4a1 1 0 0 1 1-1h3.5a1 1 0 0 1 1 1c0 1.25.2 2.45.57 3.57a1 1 0 0 1-.25 1z"/></svg>
        +312-555-0187
      </li>
      <li>
        <svg viewBox="0 0 24 24" aria-hidden="true"><rect x="3" y="5" width="18" height="14" rx="1.5" fill="none" stroke="#45b3e6" stroke-width="2"/><path d="M3.5 6l8.5 7 8.5-7" fill="none" stroke="#45b3e6" stroke-width="2"/></svg>
        daniel@brimoutreachpartners.com
      </li>
      <li>
        <svg viewBox="0 0 24 24" aria-hidden="true"><circle cx="12" cy="12" r="9.5" fill="#45b3e6"/><path d="M2.5 12h19M12 2.5v19M5 7h14M5 17h14" stroke="#1b1b1c" stroke-width="1.3" fill="none"/><ellipse cx="12" cy="12" rx="4.5" ry="9.5" fill="none" stroke="#1b1b1c" stroke-width="1.3"/></svg>
        www.brimoutreachpartners.com
      </li>
    </ul>
  </section>

</body>
</html>
```